KTR

*** Ishita see attached upload **** regarding the changes to the letter THIS IS THE NEW UPLOAD 29/07

Target Market(s)

working people
people looking to borrow $300 - $5000

Requirements
Must have
• open minded
get the Brand out there
not too many words or cluster
Nice to have
• money
people (girl) on it
logo looking vibrant
Should not have
• old style fonts

```html
<!DOCTYPE html>
<html lang="en">
<head>
<meta charset="utf-8">
<title>kitrafunds — business card</title>
<link rel="stylesheet" href="https://fonts.googleapis.com/css2?family=Questrial&family=Arimo:wght@400&display=swap">
<style>
  :root {
    --page: #e6e6e6;
    --card: #ffffff;
    --teal: #29b8c2;
    --teal-soft: #a0e3e6;
    --teal-mist: #9fd9dc;
    --ink: #5e6366;
  }
  * { box-sizing: border-box; margin: 0; padding: 0; }
  html, body {
    width: 910px; height: 1200px; overflow: hidden;
    background: var(--page);
  }
  .sheet { position: relative; width: 910px; height: 1200px; }
  .card {
    position: absolute; left: 48px; width: 817px; height: 529px;
    background: var(--card); overflow: hidden;
    font-family: "Questrial", "Century Gothic", sans-serif;
    color: var(--teal);
  }
  .card--front { top: 42px; }
  .card--back { top: 624px; }

  .disc { position: absolute; border-radius: 50%; }
  .card--front .disc {
    left: 572px; top: 30px; width: 492px; height: 492px;
    background: linear-gradient(200deg, var(--teal-soft) 0%, var(--teal-soft) 45%, var(--teal-mist) 46%, var(--teal-mist) 100%);
  }
  .card--back .disc {
    left: -250px; top: 12px; width: 504px; height: 504px;
    background: linear-gradient(20deg, var(--teal-mist) 0%, var(--teal-mist) 30%, var(--teal-soft) 31%, var(--teal-soft) 100%);
  }

  .brand { position: absolute; display: flex; align-items: center; }
  .brand__dot { border-radius: 50%; background: var(--teal); flex: none; }
  .brand__name {
    font-family: "Questrial", "Century Gothic", sans-serif;
    font-weight: 400; color: var(--teal); letter-spacing: -0.5px;
  }
  .card--front .brand { left: 26px; top: 35px; }
  .card--front .brand__dot { width: 106px; height: 106px; margin-right: 22px; }
  .card--front .brand__name { font-size: 70px; line-height: 1; }
  .card--back .brand { left: 476px; top: 32px; }
  .card--back .brand__dot { width: 56px; height: 56px; margin-right: 10px; }
  .card--back .brand__name { font-size: 38px; line-height: 1; }

  .offer { position: absolute; font-size: 23px; line-height: 29px; }
  .card--front .offer { left: 28px; top: 386px; }
  .card--front .offer--contact { top: 452px; }
  .card--back .offer { left: 269px; top: 186px; font-size: 20px; line-height: 25px; }

  .tagline { position: absolute; left: 269px; top: 134px; display: flex; align-items: flex-end; }
  .tagline__script { width: 94px; height: 42px; background: var(--teal); border-radius: 6px; margin-right: 12px; opacity: .85; }
  .tagline__text { font-size: 17px; line-height: 1; padding-bottom: 8px; }

  .contacts {
    position: absolute; right: 44px; top: 396px;
    font-family: "Arimo", Arial, sans-serif; font-size: 20px;
    list-style: none; text-align: right;
  }
  .contacts li { display: flex; justify-content: flex-end; align-items: center; height: 32px; }
  .contacts svg { width: 22px; height: 22px; margin-right: 8px; fill: var(--teal); }

  .fineprint {
    position: absolute; left: 324px; top: 502px;
    font-family: "Arimo", Arial, sans-serif; font-size: 7px; color: var(--teal);
  }
  .fineprint span { margin-right: 40px; }
  .fineprint b { font-weight: 400; color: var(--ink); margin-left: 6px; }
</style>
</head>
<body>
<div class="sheet">

  <section class="card card--front">
    <div class="disc"></div>
    <div class="brand">
      <span class="brand__dot"></span>
      <span class="brand__name">kitrafunds</span>
    </div>
    <p class="offer">$300 - $5000<br>Loans, fast &amp; simple</p>
    <p class="offer offer--contact">www.kitrafunds.com.au<br>1300 555 210</p>
  </section>

  <section class="card card--back">
    <div class="disc"></div>
    <div class="brand">
      <span class="brand__dot"></span>
      <span class="brand__name">kitrafunds</span>
    </div>
    <div class="tagline">
      <div class="tagline__script" role="img" aria-label="Hand-lettered word 'Smile' in teal script"></div>
      <span class="tagline__text">and realize your dreams</span>
    </div>
    <p class="offer">$300 - $5000<br>Loans, fast &amp; simple</p>
    <ul class="contacts">
      <li>
        <svg viewBox="0 0 24 24" aria-hidden="true"><path d="M6.6 10.8a15.1 15.1 0 0 0 6.6 6.6l2.2-2.2a1 1 0 0 1 1-.25 11.4 11.4 0 0 0 3.6.57 1 1 0 0 1 1 1V20a1 1 0 0 1-1 1A17 17 0 0 1 3 4a1 1 0 0 1 1-1h3.5a1 1 0 0 1 1 1c0 1.25.2 2.45.57 3.57a1 1 0 0 1-.25 1z"/></svg>
        1300 555 210
      </li>
      <li>
        <svg viewBox="0 0 24 24" aria-hidden="true"><path d="M2 5h20v14H2z M3 6l9 7 9-7" fill="var(--teal)" stroke="#fff" stroke-width="1.2"/></svg>
        hello@kitrafunds.com.au
      </li>
      <li>
        <svg viewBox="0 0 24 24" aria-hidden="true"><circle cx="12" cy="12" r="10"/><path d="M2 12h20M12 2v20M5 6.5h14M5 17.5h14M12 2c-4 4-4 16 0 20M12 2c4 4 4 16 0 20" fill="none" stroke="#fff" stroke-width="1"/></svg>
        www.kitrafunds.com.au
      </li>
    </ul>
    <p class="fineprint"><span>Australian Credit Licence<b>48210</b></span><span>ABN<b>7730019</b></span></p>
  </section>

</div>
</body>
</html>
```